Ledgerwise Business Card Design

Business Card Design for new business called Ledgerwise focused on selling business software to small and medium size companies who have outgrown Tallymark. Similar companies would be Tallymark, Nuvo, CoreFlow. Also Dealharbor would be good to look at for additional ideas around look and feel.

Target Market(s)

Business to Business

Industry/Entity Type

Information Technology

Contact Information for Business Card

Standard Business Card Information

Font styles to use
Sans Serif

```html
<!DOCTYPE html>
<html lang="en">
<head>
<meta charset="utf-8">
<title>Ledgerwise Stationery</title>
<link href="https://fonts.googleapis.com/css2?family=Archivo:wght@400;500;600;700&display=swap" rel="stylesheet">
<style>
:root{
  --stage:#3a3a3c;
  --navy:#0e5185;
  --orange:#f58220;
  --paper:#ffffff;
  --card-light:#ebebed;
  --ink-light:#ffffff;
}
*{margin:0;padding:0;box-sizing:border-box}
html,body{width:1200px;height:1199px;overflow:hidden}
body{background:var(--stage);font-family:"Archivo",Arial,sans-serif;position:relative}
.sheet,.card{position:absolute;overflow:hidden}
.shape{position:absolute;inset:0;width:100%;height:100%}
.letterhead{left:52px;top:141px;width:648px;height:916px;background:var(--paper)}
.brand{position:absolute;display:flex;align-items:center;gap:8px;font-weight:700;letter-spacing:-0.5px;white-space:nowrap}
.brand-dot{border-radius:50%;flex:none}
.letterhead .brand{left:46px;top:56px;font-size:30px;color:var(--navy)}
.letterhead .brand-dot{width:22px;height:22px;background:var(--orange)}
.letterhead-address{position:absolute;right:33px;top:42px;text-align:right;color:var(--ink-light);font-size:11.5px;font-weight:600;line-height:16px}
.letterhead-contacts{position:absolute;left:33px;top:825px;color:var(--ink-light);font-size:11.5px;font-weight:500;line-height:15.5px}
.card{width:420px;height:248px}
.card-front{left:729px;top:275px;background:var(--card-light)}
.card-back{left:729px;top:576px}
.name-tag{position:absolute;left:160px;top:52px;width:130px;height:24px;color:var(--ink-light);text-align:right;padding-right:26px}
.name-tag .name{display:block;font-size:10.5px;font-weight:500;line-height:12px;padding-top:1px}
.name-tag .role{display:block;font-size:8px;line-height:9px}
.contact-list{position:absolute;left:23px;top:98px;list-style:none}
.contact-list li{display:flex;align-items:center;gap:5px;height:25.5px;color:var(--ink-light);font-size:9.5px;font-weight:500}
.contact-list li.address{font-size:8px;line-height:10px;height:28px}
.contact-icon{width:20px;height:20px;flex:none}
.card-front .brand{left:276px;top:183px;font-size:19px;color:var(--navy)}
.card-front .brand-dot{width:14px;height:14px;background:var(--orange)}
.card-back .brand{left:116px;top:110px;font-size:27px;color:var(--ink-light)}
.card-back .brand-dot{width:18px;height:18px;background:var(--ink-light)}
</style>
</head>
<body>

<section class="sheet letterhead">
  <svg class="shape" viewBox="0 0 648 916" aria-hidden="true">
    <polygon points="306,0 648,0 648,242" fill="var(--orange)"/>
    <polygon points="0,674 0,916 343,916" fill="var(--navy)"/>
  </svg>
  <div class="brand"><span>Ledgerwise</span><span class="brand-dot"></span></div>
  <p class="letterhead-address">Street # 6, Road Lorem Ipsum<br>City, Region, Country. Postal Code</p>
  <p class="letterhead-contacts">+1 555 014 2280<br>+1 555 014 2280<br>info@ledgerwise.com<br>www.ledgerwise.com</p>
</section>

<section class="card card-front">
  <svg class="shape" viewBox="0 0 420 248" aria-hidden="true">
    <polygon points="0,0 122,0 289,248 0,248" fill="var(--navy)"/>
    <polygon points="156,46 276,46 288,76 172,76" fill="var(--orange)"/>
  </svg>
  <div class="name-tag"><span class="name">NAME SURNAME</span><span class="role">Role</span></div>
  <ul class="contact-list">
    <li><svg class="contact-icon" viewBox="0 0 20 20"><circle cx="10" cy="10" r="10" fill="var(--orange)"/><rect x="7" y="4.5" width="6" height="11" rx="1" fill="none" stroke="var(--navy)" stroke-width="1.3"/></svg>+1 555 019 4461</li>
    <li><svg class="contact-icon" viewBox="0 0 20 20"><circle cx="10" cy="10" r="10" fill="var(--orange)"/><path d="M5 9c0-3 10-3 10 0v1h-3V8.5H8V10H5z M6 11h8l1 4H5z" fill="var(--navy)"/></svg>+1 555 014 2280</li>
    <li><svg class="contact-icon" viewBox="0 0 20 20"><circle cx="10" cy="10" r="10" fill="var(--orange)"/><rect x="5" y="6.5" width="10" height="7" fill="none" stroke="var(--navy)" stroke-width="1.2"/><path d="M5 6.5l5 4 5-4" fill="none" stroke="var(--navy)" stroke-width="1.2"/></svg>info@ledgerwise.com</li>
    <li><svg class="contact-icon" viewBox="0 0 20 20"><circle cx="10" cy="10" r="10" fill="var(--orange)"/><circle cx="10" cy="10" r="5" fill="none" stroke="var(--navy)" stroke-width="1.1"/><path d="M5 10h10M10 5v10M6.5 7h7M6.5 13h7" stroke="var(--navy)" stroke-width="0.9"/></svg>www.ledgerwise.com</li>
    <li class="address"><svg class="contact-icon" viewBox="0 0 20 20"><circle cx="10" cy="10" r="10" fill="var(--orange)"/><path d="M10 15.5s-4-4.2-4-7a4 4 0 0 1 8 0c0 2.8-4 7-4 7z" fill="var(--navy)"/><circle cx="10" cy="8.5" r="1.4" fill="var(--orange)"/></svg><span>Street # 6, Road Lorem Ipsum<br>City, Region, Country. Postal Code</span></li>
  </ul>
  <div class="brand"><span>Ledgerwise</span><span class="brand-dot"></span></div>
</section>

<section class="card card-back">
  <svg class="shape" viewBox="0 0 420 248" aria-hidden="true">
    <rect width="420" height="248" fill="var(--orange)"/>
    <polygon points="0,0 303,0 136,248 0,248" fill="var(--navy)"/>
  </svg>
  <div class="brand"><span>Ledgerwise</span><span class="brand-dot"></span></div>
</section>

</body>
</html>
```